Professional looking website for solo practitioner law practice

I have recently started up my new law practice. Currently there is just myself practicing here. I would like to have a website that provides my contact information, a map, and the different areas of law that I practice in, being Family Litigation, Wills & Estates, Corporate/Commerical, and Real Estate. I recently had a logo designed so I would like the colours of my website to be congruent with that and include the logo.
I am located in Edmonton, Alberta.

Reason: I will be away for the next few days.

Target Market(s)

individuals and families with an income of $50K+, mostly those looking for family lawyer re divorce, child support, custody and parenting, spousal support.

Industry/Entity Type

Lawyer

Number of Pages Required

4 page

Font styles to use
Serif

Colors
0355a3

Requirements
Must have
• Contact information, ability to email me, background picture(s) that are professional and fit with the legal services theme/service provided but are not single individual lawyers, gavels, or court houses. Need to have click to change the text to include information on Family Litigation, Wills & Estates, Corporate/Commercial, and Real Estate
Nice to have
• contact box
Should not have
• blog, sans serif text, testimonials, news

```html
<!DOCTYPE html>
<html lang="en">
<head>
<meta charset="utf-8">
<title>Marlowe Quinn Law Office</title>
<link rel="stylesheet" href="https://fonts.googleapis.com/css2?family=Cinzel:wght@400;700&family=Raleway:wght@400;500&family=Open+Sans:wght@400;600&display=swap">
<style>
:root{
  --brand:#0355a3;
  --brand-deep:#1b3a84;
  --text:#666a70;
  --header-top:#ffffff;
  --header-bottom:#eef0f2;
  --footer:#0a0d14;
  --ink:#0b0b0c;
  --white:#ffffff;
  --teal:#0f6e82;
}
*{box-sizing:border-box;margin:0;padding:0}
html,body{width:1200px;height:1086px;overflow:hidden;background:#fff}
body{position:relative;font-family:'Raleway',sans-serif;color:var(--text)}
.site-header{position:absolute;left:0;top:0;width:1200px;height:86px;background:linear-gradient(var(--header-top),var(--header-bottom))}
.brand{position:absolute;left:141px;top:14px;display:flex;align-items:center;gap:12px}
.brand-mark{width:58px;height:58px;border:3px solid var(--brand-deep)}
.brand-name{font-family:'Cinzel',serif;font-weight:700;font-size:24px;line-height:1.05;color:var(--brand-deep)}
.brand-name small{display:block;font-size:13px;letter-spacing:4px;text-align:center}
.main-nav{position:absolute;right:162px;top:40px;display:flex;gap:0;font-family:'Cinzel',serif;font-size:13px;letter-spacing:.5px}
.main-nav a,.footer-nav a{text-decoration:none;color:inherit}
.main-nav a{color:var(--brand)}
.main-nav .sep,.footer-nav .sep{margin:0 18px}
.main-nav .sep{color:var(--brand)}
.section-title{position:absolute;left:169px;font-family:'Cinzel',serif;font-weight:400;font-size:30px;color:var(--brand);display:flex;align-items:center;gap:14px}
.section-title::after{content:"";display:block;width:114px;height:1px;background:var(--brand)}
.about-title{top:117px}
.team-title{top:383px}
.about-text{position:absolute;left:170px;top:165px;width:578px;font-size:12px;line-height:19.2px}
.about-text p+p{margin-top:19.2px}
.about-photo{position:absolute;left:789px;top:118px;width:257px;height:246px;background:linear-gradient(135deg,#c9d3d8,#8c9196 55%,#4b4f52)}
.team{position:absolute;top:442px;left:159px;display:flex;gap:17px}
.member{width:208px;height:235px;position:relative}
.member-1{background:linear-gradient(#3a3f45,#1e2226)}
.member-2{background:linear-gradient(#c9c3c0,#b67b5d 60%,#d2453e)}
.member-3{background:linear-gradient(#7e7874,#4e4a48 60%,#2a2b2e)}
.member-4{background:linear-gradient(#d6d5d4,#9a7f6f 60%,#2b2a2b)}
.member-overlay{position:absolute;inset:0;background:rgba(3,85,163,.72);color:var(--white);text-align:center;font-family:'Open Sans',sans-serif}
.plus{position:absolute;left:84px;top:55px;width:40px;height:36px;background:var(--teal);display:flex;align-items:center;justify-content:center}
.member-name{position:absolute;top:101px;left:0;right:0;font-size:20px;font-weight:400}
.member-bio{position:absolute;top:136px;left:18px;right:18px;font-size:11px;font-weight:600;line-height:19.2px}
.contact{position:absolute;left:0;top:714px;width:456px;height:312px;background:var(--brand)}
.contact h2{position:absolute;left:169px;top:30px;font-family:'Raleway',sans-serif;font-weight:400;font-size:16px;color:var(--white)}
.field{position:absolute;left:172px;width:241px;height:26px;background:var(--white);border:1px solid #cfd6de;font-family:'Raleway',sans-serif;font-size:11.5px;color:#444;padding:6px 15px}
.f-name{top:66px}.f-phone{top:107px}.f-email{top:148px}.f-comment{top:189px;height:50px}
.send{position:absolute;left:174px;top:249px;width:239px;height:36px;background:var(--ink);color:var(--white);font-family:'Raleway',sans-serif;font-size:13.5px;display:flex;align-items:center;justify-content:center;gap:14px;box-shadow:0 2px 0 #02336a}
.map{position:absolute;left:456px;top:714px;width:744px;height:312px;background:linear-gradient(120deg,#eceae6,#e7e4df 50%,#ebe8e3)}
.site-footer{position:absolute;left:0;top:1026px;width:1200px;height:60px;background:var(--footer);color:var(--white)}
.footer-nav{position:absolute;left:170px;top:23px;display:flex;font-family:'Cinzel',serif;font-size:13px;letter-spacing:.5px}
.copyright{position:absolute;left:877px;top:24px;font-size:11px;color:#d8d8d8}
</style>
</head>
<body>
<header class="site-header">
  <div class="brand">
    <div class="brand-mark"></div>
    <div class="brand-name">Marlowe Quinn<small>Law Office</small></div>
  </div>
  <nav class="main-nav">
    <a href="#">HOME</a><span class="sep">-</span>
    <a href="#">ABOUT US</a><span class="sep">-</span>
    <a href="#">SERVICES</a><span class="sep">-</span>
    <a href="#">CONTACT US</a>
  </nav>
</header>

<h1 class="section-title about-title">ABOUT US</h1>
<div class="about-text">
  <p>A consectetur a aliquet a enim sit sit litora libero proin ad donec a cubilia potenti posuere. Posuere nam nisl sit amet id tincidunt augue a morbi mauris a euismod a sociis at. Ridiculus et leo nec class hac condimentum iaculis vestibulum eget laoreet luctus scelerisque est mus nisi laoreet euismod in primis aliquam metus dictum parturient parturient. Adipiscing viverra nulla proin tincidunt fusce torquent a a adipiscing inceptos a a massa adipiscing facilisi luctus ad convallis suspendisse.</p>
  <p>Litora quisque per pharetra feugiat quisque consectetur neque adipiscing scelerisque hac maecenas a posuere blandit a suscipit parturient urna. Arcu parturient malesuada imperdiet ornare ultricies porttitor scelerisque vestibulum tortor mi aliquet ullamcorper mi conubia vivamus.</p>
</div>
<div class="about-photo" role="img" aria-label="Photo of a team meeting around a table in a bright office"></div>

<h2 class="section-title team-title">Our Team</h2>
<div class="team">
  <div class="member member-1" role="img" aria-label="Portrait photo of a staff member">
    <div class="member-overlay">
      <div class="plus"><svg width="16" height="16" viewBox="0 0 16 16"><path d="M6 0h4v6h6v4h-6v6H6v-6H0V6h6z" fill="#fff"/></svg></div>
      <div class="member-name">Staff Name</div>
      <div class="member-bio">Imperdiet mi primis natoque scelerisque eget neque pharetra nam adipiscing et condimentum nam class lobortis adipiscing a.</div>
    </div>
  </div>
  <div class="member member-2" role="img" aria-label="Portrait photo of a staff member"></div>
  <div class="member member-3" role="img" aria-label="Portrait photo of a staff member"></div>
  <div class="member member-4" role="img" aria-label="Portrait photo of a staff member"></div>
</div>

<section class="contact">
  <h2>GET IN TOUCH</h2>
  <div class="field f-name">Enter your name</div>
  <div class="field f-phone">Phone Number</div>
  <div class="field f-email">Email</div>
  <div class="field f-comment">Comment</div>
  <div class="send">SEND YOUR ENQUIRE
    <svg width="16" height="14" viewBox="0 0 16 14"><path d="M16 0L0 6l4.5 1.6L13 2 6 8.5V14l2.8-3.6L12 12z" fill="#fff"/></svg>
  </div>
</section>
<div class="map" role="img" aria-label="Street map showing the office location"></div>

<footer class="site-footer">
  <nav class="footer-nav">
    <a href="#">HOME</a><span class="sep">-</span>
    <a href="#">ABOUT US</a><span class="sep">-</span>
    <a href="#">SERVICES</a><span class="sep">-</span>
    <a href="#">CONTACT US</a>
  </nav>
  <div class="copyright">© 2016 - www.companyname.com</div>
</footer>
</body>
</html>
```